New Advertising Company Business Card

A two sided business card. One side with logo only and the other side with my information and maybe my logo again. Looking for something unique and creative, but not too busy. Info would include my name(Marcus Feldon), President, phone number, address, email address, and website. LOGO IS THE BLUE AND WHITE ONE.

Target Market(s)

CEO/VP Level Audience

Industry/Entity Type

Business

Contact Information for Business Card

In Description.

```html
<!DOCTYPE html>
<html lang="en">
<head>
<meta charset="utf-8">
<title>Harbor Advertising – Business Card</title>
<link rel="stylesheet" href="https://fonts.googleapis.com/css2?family=Montserrat:wght@600&family=Roboto+Condensed:wght@400;700&display=swap">
<style>
  :root {
    --page-bg: #ece8e2;
    --navy-deep: #031a4a;
    --navy-mid: #083a8a;
    --blue-bright: #1a8ae6;
    --band-blue: #1f6fc9;
    --band-dark: #0d4ea6;
    --card-light: #f3f4f4;
    --ink-dark: #333438;
    --white: #ffffff;
  }
  * { box-sizing: border-box; margin: 0; padding: 0; }
  html, body { width: 1200px; height: 1200px; overflow: hidden; }
  body { background: var(--page-bg); position: relative; font-family: "Roboto Condensed", Arial, sans-serif; }

  .card {
    position: absolute;
    left: 263px;
    width: 674px;
    height: 434px;
    border-radius: 120px 0 120px 0;
    overflow: hidden;
    box-shadow: 0 6px 16px rgba(0,0,0,0.18);
  }
  .card--front {
    top: 125px;
    background:
      radial-gradient(ellipse 60% 55% at 50% 0%, var(--blue-bright) 0%, rgba(26,138,230,0) 100%),
      linear-gradient(180deg, var(--navy-mid) 0%, var(--navy-deep) 85%);
  }
  .card--back { top: 600px; background: var(--card-light); }

  .wordmark {
    position: absolute;
    left: 0; right: 0;
    text-align: center;
    font-family: "Montserrat", Arial, sans-serif;
    font-weight: 600;
    line-height: 1;
  }
  .wordmark__name { display: block; font-size: 60px; letter-spacing: 3px; }
  .wordmark__tag { display: block; font-size: 22px; letter-spacing: 6px; margin-top: 10px; }
  .card--front .wordmark { top: 160px; color: var(--white); }
  .card--back .wordmark { top: 100px; color: var(--ink-dark); }

  .info-band {
    position: absolute;
    left: 0; right: 0; bottom: 0;
    height: 160px;
    background: radial-gradient(ellipse 50% 80% at 25% 40%, #3f8fe0 0%, rgba(63,143,224,0) 100%),
                linear-gradient(90deg, var(--band-dark), var(--band-blue) 50%, var(--band-dark));
    color: var(--white);
  }
  .holder { position: absolute; left: 28px; top: 24px; }
  .holder__name { font-weight: 700; font-size: 35px; line-height: 1; letter-spacing: 0.5px; }
  .holder__title { font-size: 20px; margin-top: 4px; }

  .contact-list {
    position: absolute;
    left: 388px; top: 24px;
    list-style: none;
    font-size: 14px;
    line-height: 17px;
  }
  .contact-list li { display: flex; align-items: flex-start; margin-bottom: 6px; }
  .contact-list svg { flex: none; width: 17px; height: 17px; margin-right: 9px; }
</style>
</head>
<body>

  <section class="card card--front" aria-label="Card front">
    <div class="wordmark">
      <span class="wordmark__name">HARBOR</span>
      <span class="wordmark__tag">ADVERTISING</span>
    </div>
  </section>

  <section class="card card--back" aria-label="Card back">
    <div class="wordmark">
      <span class="wordmark__name">HARBOR</span>
      <span class="wordmark__tag">ADVERTISING</span>
    </div>

    <div class="info-band">
      <div class="holder">
        <p class="holder__name">MARCUS FELDON</p>
        <p class="holder__title">PRESIDENT</p>
      </div>

      <ul class="contact-list">
        <li>
          <svg viewBox="0 0 20 20" aria-hidden="true"><circle cx="10" cy="10" r="9" fill="none" stroke="#fff" stroke-width="1.4"/><path d="M10 4.5a3.5 3.5 0 0 0-3.5 3.5c0 2.6 3.5 6.5 3.5 6.5s3.5-3.9 3.5-6.5A3.5 3.5 0 0 0 10 4.5z" fill="#fff"/><circle cx="10" cy="8" r="1.3" fill="#1f6fc9"/></svg>
          <span>418 Linden Avenue, 9th Floor<br>Riverton, NJ 08077</span>
        </li>
        <li>
          <svg viewBox="0 0 20 20" aria-hidden="true"><circle cx="10" cy="10" r="9" fill="none" stroke="#fff" stroke-width="1.4"/><path d="M6.5 5.5l2 0 1 2.5-1.3 1a6 6 0 0 0 2.8 2.8l1-1.3 2.5 1v2a1 1 0 0 1-1 1A8.5 8.5 0 0 1 5.5 6.5a1 1 0 0 1 1-1z" fill="#fff"/></svg>
          <span>0123-555-870</span>
        </li>
        <li>
          <svg viewBox="0 0 20 20" aria-hidden="true"><circle cx="10" cy="10" r="9" fill="none" stroke="#fff" stroke-width="1.4"/><rect x="5" y="6.5" width="10" height="7" fill="#fff"/><path d="M5 6.8l5 3.8 5-3.8" fill="none" stroke="#1f6fc9" stroke-width="1"/></svg>
          <span>hello@harborads.com</span>
        </li>
        <li>
          <svg viewBox="0 0 20 20" aria-hidden="true"><circle cx="10" cy="10" r="9" fill="none" stroke="#fff" stroke-width="1.4"/><circle cx="10" cy="10" r="5" fill="none" stroke="#fff" stroke-width="1.1"/><ellipse cx="10" cy="10" rx="2.2" ry="5" fill="none" stroke="#fff" stroke-width="1"/><path d="M5 10h10" stroke="#fff" stroke-width="1"/></svg>
          <span>harbor.advertising.com</span>
        </li>
      </ul>
    </div>
  </section>

</body>
</html>
```